Company PowerPoint Presentation Template

I am looking for a business powerpoint template tailored to my company that specializes in permafrost services for the mining, transportation, and oil & gas industries. The template would be used to present project findings from studies completed for our clients. I am looking for a crisp, technical, professional business look to the template. Our business is located in North America and English is the primary language used to communicate our work. Complimentary colors associated with the business is blue (RGB, 0,112,192) or something similar in color.

```html
<!DOCTYPE html>
<html lang="en">
<head>
<meta charset="UTF-8">
<title>Your Topic – Alder Bay Group</title>
<link href="https://fonts.googleapis.com/css2?family=Poppins:wght@200;300;400;600&display=swap" rel="stylesheet">
<style>
  :root {
    --sky: #0aa0e2;
    --mid: #0a7dd0;
    --navy: #0053b1;
    --white: #ffffff;
    --photo-a: #9fb8cf;
    --photo-b: #4f6a86;
    --photo-c: #26384f;
  }
  * { margin: 0; padding: 0; box-sizing: border-box; }
  html, body { width: 1200px; height: 675px; overflow: hidden; }
  body { font-family: "Poppins", Arial, sans-serif; color: var(--white); background: var(--sky); }
  .slide { position: relative; width: 1200px; height: 675px; overflow: hidden; background: var(--sky); }
  .backdrop { position: absolute; inset: 0; }
  .site-photo {
    position: absolute; left: 0; top: 0; width: 406px; height: 675px;
    background: linear-gradient(160deg, var(--photo-a) 0%, var(--photo-b) 45%, var(--photo-c) 75%, #5d6f82 100%);
  }
  .brand {
    position: absolute; left: 40px; top: 612px;
    font-weight: 600; font-size: 21px; line-height: 1;
    color: var(--white);
  }
  .heading { position: absolute; right: 72px; top: 60px; width: 470px; text-align: right; }
  .heading h1 { font-weight: 600; font-size: 35px; line-height: 1; letter-spacing: 0.3px; }
  .heading p { margin-top: 12px; font-weight: 300; font-size: 6.9px; line-height: 8.3px; }
  .item { position: absolute; width: 160px; }
  .item .number { font-weight: 200; font-size: 118px; line-height: 1; letter-spacing: -2px; margin-left: -6px; }
  .item .rule { height: 1.5px; margin-top: 2px; background: var(--white); }
  .item p { font-weight: 300; font-size: 5.6px; line-height: 6.8px; margin-top: 19px; }
  .item-1 { left: 483px; top: 190px; }
  .item-2 { left: 732px; top: 190px; }
  .item-2 .number { margin-left: -17px; }
  .item-3 { left: 960px; top: 190px; }
  .item-4 { left: 483px; top: 402px; }
  .item-5 { left: 722px; top: 402px; }
  .item-6 { left: 960px; top: 402px; }
</style>
</head>
<body>
<main class="slide">
  <svg class="backdrop" width="1200" height="675" viewBox="0 0 1200 675" aria-hidden="true">
    <polygon points="484,0 1200,0 1200,363 1043,158" fill="var(--mid)"/>
    <polygon points="915,0 1200,0 1200,207 1043,158" fill="var(--navy)"/>
    <polygon points="406,484 589,675 406,675" fill="var(--mid)"/>
  </svg>

  <div class="site-photo" role="img" aria-label="Large bucket-wheel excavator standing in an open-pit mine with sandy slopes, tinted blue"></div>
  <div class="brand">Alder Bay Group</div>

  <header class="heading">
    <h1>YOUR TOPIC</h1>
    <p>Lorem ipsum dolor sit amet, consectetuer adipiscing elit, sed diam nonummy nibh euismod tincidunt ut laoreet dolore magna aliquam erat volutpat. Ut wisi enim ad minim veniam, quis nostrud exerci tation ullamcorper suscipit lobortis nisl ut aliquip ex ea commodo consequat. Duis autem vel eum iriu</p>
  </header>

  <section class="item item-1">
    <div class="number">01</div><div class="rule"></div>
    <p>Lorem ipsum dolor sit amet, consectetuer adipiscing elit, sed diam nonummy nibh euismod tincidunt ut laoreet dolore magna aliquam erat volutpat. Ut wisi enim ad minim veniam, quis nostrud exerci tation ullamcorper suscipit lobortis nisl ut aliquip ex ea commodo consequat. Duis autem vel eum iriu</p>
  </section>
  <section class="item item-2">
    <div class="number">02</div><div class="rule"></div>
    <p>Lorem ipsum dolor sit amet, consectetuer adipiscing elit, sed diam nonummy nibh euismod tincidunt ut laoreet dolore magna aliquam erat vo</p>
  </section>
  <section class="item item-3">
    <div class="number">03</div><div class="rule"></div>
    <p>Lorem ipsum dolor sit amet, consectetuer adipiscing elit, sed diam nonummy nibh euismod tincidunt ut laoreet dolore magna aliquam erat volutpat. Ut wisi enim ad minim veniam, quis nostrud</p>
  </section>
  <section class="item item-4">
    <div class="number">04</div><div class="rule"></div>
    <p>Lorem ipsum dolor sit amet, consectetuer adipiscing elit, sed diam nonummy nibh euismod tincidunt ut laoreet dolore magna aliquam erat volutpat. Ut wisi enim ad minim veniam, quis nostrud exerci tation ullamcorper suscipit lobortis nisl ut aliquip ex ea commod</p>
  </section>
  <section class="item item-5">
    <div class="number">05</div><div class="rule"></div>
    <p>Lorem ipsum dolor sit amet, consectetuer adipiscing elit, sed diam nonummy nibh euismod tincidunt ut laoreet dolore magna aliquam erat volutpat. Ut wisi enim ad minim veniam, quis nostrud exerci tation ullamcorper suscipit lobortis nisl ut aliquip ex ea commodo consequat. Duis aut</p>
  </section>
  <section class="item item-6">
    <div class="number">06</div><div class="rule"></div>
    <p>Lorem ipsum dolor sit amet, consectetuer adipiscing elit, sed diam nonummy nibh euismod tincidunt ut laoreet dolore magna aliquam erat volutpat. Ut wisi enim ad minim veniam, quis nostrud exerci tation ullamcorper suscipit lobortis nisl ut aliquip ex</p>
  </section>
</main>
</body>
</html>
```